Real Estate - Property Management Business needs a Landlords Handbook designed

We need a landlord's handbook designed. We are a specialist property management business. The text and logos are there. The book needs images and to present more as a book. We would like to see designs that use orange, grey and white.
Our website is www.tallowbrook.com.au to give you an idea of our brand.

Target Market(s)

Professional couples - property investors

Industry/Entity Type

Real Estate

Font styles to use
Sans Serif

Colors
ffffff
1b1b1b
f37122

Requirements
Must have
• Images of property owners and applicable images
Nice to have
• The Pemberlys owner handbook is a guide to show you what I am looking for
Should not have
• This needs to look professional. No cartoon images

```html
<!DOCTYPE html>
<html lang="en">
<head>
<meta charset="utf-8">
<title>Tallowbrook Landlords Handbook</title>
<link href="https://fonts.googleapis.com/css2?family=Source+Sans+3:wght@400;600;700&family=Roboto+Condensed:wght@700&display=swap" rel="stylesheet">
<style>
:root{
  --orange:#f37122;
  --ink:#1b1b1b;
  --grey:#6d6e71;
  --paper:#ffffff;
  --backdrop:#e6e6e7;
  --pool:#3fa9d6;
  --pool-deep:#1f6f9c;
  --navy:#1d3f7a;
}
*{box-sizing:border-box;margin:0;padding:0}
html,body{width:898px;height:1200px;overflow:hidden}
body{background:var(--backdrop);font-family:"Source Sans 3",Arial,sans-serif;color:var(--ink);position:relative}
.page{position:absolute;background:var(--paper);overflow:hidden;box-shadow:0 2px 6px rgba(0,0,0,.15)}
.photo{position:absolute}
.folio{position:absolute;bottom:10px;font-size:7px;color:var(--ink);border-bottom:1px solid var(--ink);padding-bottom:1px}
.page-num{position:absolute;bottom:0;width:12px;height:16px;background:var(--ink);color:#fff;font-size:6px;text-align:center;line-height:16px}

/* intro spread */
.intro-left{left:40px;top:110px;width:230px;height:325px}
.intro-right{left:270px;top:110px;width:230px;height:325px}
.intro-left .photo{inset:0 0 40px 0;background:linear-gradient(160deg,#bfe0ee 0%,#5fa9c9 45%,#2d6f8f 70%,#4fb4df 100%)}
.intro-right .photo{inset:0 0 40px 0;background:linear-gradient(200deg,#d8edf5 0%,#6db3cf 50%,#3b8fb8 100%)}
.intro-panel{position:absolute;left:0;right:0;top:190px;height:78px;background:var(--orange);color:#fff;font-size:8.5px;line-height:1.4;padding:10px 14px}

/* cover */
.cover{left:548px;top:70px;width:320px;height:452px}
.cover .photo{left:14px;right:14px;top:14px;height:330px;background:linear-gradient(120deg,#f3f1ee 0%,#e9e3dc 40%,#c94a3d 55%,#d9d2c9 75%,#5b6576 100%)}
.brand{position:absolute;display:flex;align-items:center;gap:6px;font-weight:700;color:var(--orange)}
.brand-mark{width:14px;height:14px;background:var(--orange)}
.cover .brand{left:30px;top:380px;font-size:26px}
.badges{position:absolute;right:24px;top:26px;display:flex;gap:4px}
.badge{width:26px;height:12px;background:#fff;border:1px solid #c9c9c9}
.badge.red{background:#d6333b;border-color:#d6333b}

/* main spread */
.spread-left{left:49px;top:590px;width:400px;height:570px}
.spread-right{left:449px;top:590px;width:400px;height:570px}
.spread-left .photo{left:16px;right:0;top:20px;height:330px;background:linear-gradient(150deg,#6fc7ee 0%,var(--pool) 45%,var(--pool-deep) 100%)}
.section-title{position:absolute;left:40px;top:40px;color:#fff;font-family:"Roboto Condensed",Arial,sans-serif;font-size:17px;letter-spacing:.3px}
.pool-text{position:absolute;left:16px;right:0;top:350px;height:140px;background:var(--orange);color:#fff;font-size:8px;line-height:1.45;padding:12px 20px}
.pool-text p+p{margin-top:8px}
.pool-band{position:absolute;left:16px;right:0;top:490px;height:20px;background:var(--navy)}
.spread-left .folio{right:24px}
.spread-left .page-num{left:40px}

.imprint{position:absolute;left:24px;top:34px;font-size:5.5px;color:var(--grey);line-height:1.3}
.imprint b{color:var(--orange);font-weight:600}
.spread-right .badges{top:34px;right:40px}
.rule{position:absolute;left:24px;right:40px;top:58px;height:1px;background:#bdbdbd}
.spread-right .photo{left:0;right:0;top:68px;height:170px;background:linear-gradient(200deg,#6b5a4a 0%,#d8d2c8 40%,#f4f1ec 70%,#c9bfae 100%)}
.tag{position:absolute;left:24px;top:160px;background:var(--orange);color:#fff;font-family:"Roboto Condensed",Arial,sans-serif;font-size:14px;line-height:1.15;padding:6px 14px 5px 18px}
.cols{position:absolute;left:24px;right:40px;top:255px;display:flex;gap:14px;font-size:6.5px;line-height:1.5;color:#444}
.col{flex:1}
.col h4{color:var(--orange);font-size:7px;font-weight:600;margin:10px 0 6px}
.col h4:first-child{margin-top:0}
.col p{margin-bottom:7px;text-align:justify}
.spread-right .folio{left:24px}
.spread-right .page-num{right:40px}
</style>
</head>
<body>

<section class="page intro-left" aria-label="Handbook opening page">
  <div class="photo" role="img" aria-label="Photo of a modern home with a curved swimming pool at dusk"></div>
  <span class="folio" style="right:18px">www.tallowbrook.com.au</span>
</section>
<section class="page intro-right" aria-label="Handbook welcome page">
  <div class="photo" role="img" aria-label="Photo continuing the modern home and pool scene"></div>
  <div class="intro-panel">Tallowbrook is a dynamic and energetic specialist property manager, providing the best service, advice and support to you and your investment, with our team's ongoing learning and technology to help our clients thrive.</div>
  <span class="folio" style="left:18px">www.tallowbrook.com.au</span>
</section>

<section class="page cover" aria-label="Handbook cover">
  <div class="photo" role="img" aria-label="Photo of a property owner shaking hands with an agent over a model house and plans"></div>
  <div class="badges"><span class="badge"></span><span class="badge red"></span></div>
  <div class="brand"><span class="brand-mark"></span>Tallowbrook</div>
</section>

<section class="page spread-left" aria-label="Pool safety laws page">
  <div class="photo" role="img" aria-label="Photo of a smiling child floating in a swimming pool"></div>
  <h2 class="section-title">POOL SAFETY LAWS</h2>
  <div class="pool-text">
    <p>The Building Act of Queensland sets out the legal requirements for pools and spas. A rental property (house or unit) with a pool cannot be rented without a pool safety certificate. In addition, all pools and spas in Queensland (regardless if they are a rental property) must be registered on the Queensland Government pool register. All Queensland properties, which includes owner occupied, must have a pool safety certificate as at 30 November 2015.</p>
    <p>Shared pools (units generally) are required to also have the pool safety certificate in a conspicuous position at the property or on the pool gate. We recommend that you speak with the body corporate for more information in this regard. Pool safety certificates are valid for two years from the date of issue for non-shared pools, and one year for shared pools.</p>
  </div>
  <div class="pool-band"></div>
  <span class="page-num">20</span>
  <span class="folio">www.tallowbrook.com.au</span>
</section>

<section class="page spread-right" aria-label="Tenants rights and obligations page">
  <p class="imprint">© Tallowbrook Owner Guide is a product of<br><b>Tallowbrook Academy Pty Ltd</b></p>
  <div class="badges"><span class="badge"></span><span class="badge red"></span></div>
  <div class="rule"></div>
  <div class="photo" role="img" aria-label="Photo of a pen resting on a rental application form"></div>
  <h2 class="tag">TENANTS RIGHT<br>AND OBLIGATIONS</h2>
  <div class="cols">
    <div class="col">
      <p>Tenant have obligations during the tenancy such as keeping the premises clean during the tenancy having regard to how they found it as per the entry condition report, ensure that they don't cause damage to the property, don't use the property for illegal purposes, do not disturb the neighbourhood and of course, to pay their rent accordingly. If the tenant fails in any of these statutory obligations, breach notices under tenancy legislation can be served to them. Breaches are discussed further in the document. General legislative information is provided below for your interest and information.</p>
      <h4>184 Tenant's use of premises</h4>
      <p>The tenant must not—<br>(a) use the premises for an illegal purpose; or<br>(b) cause a nuisance by the use of the premises; or<br>(c) interfere with the reasonable peace, comfort or privacy of a neighbour of the tenant.</p>
    </div>
    <div class="col">
      <h4>188 Tenant's obligations generally</h4>
      <p>(1) This section does not apply to an agreement if—(a) the premises are moveable dwelling premises consisting only of the site for the dwelling; and (b) the tenancy is a long tenancy (moveable dwelling).</p>
      <p>(2) The tenant must keep the premises and inclusions clean, having regard to their condition at the start of the tenancy.</p>
      <p>(3) The tenant must not maliciously damage, or allow someone else to maliciously damage, the premises or inclusions.</p>
      <p>(4) At the end of the tenancy, the tenant must leave the premises and inclusions, as far as possible, in the same condition they were in at the start of the tenancy, fair wear and tear excepted.</p>
      <p>If tenants wish to attach fixtures such as picture</p>
    </div>
  </div>
  <span class="folio">www.tallowbrook.com.au</span>
  <span class="page-num">21</span>
</section>

</body>
</html>
```